Bramble Hollow Networks - Electrical

We need flyers for electrical services.
Areas of work include new builds, office fitouts, switchboard upgrades, installation of ceiling fans, powerpoint and downlight upgrades, home theatre and AV systems, all exterior and emergency work. Free quotes
We would like to see designs with the colour Red with a young and modern design. Licence No: 63914K must be included and call Leopold on 0438917062.

Colors
ec1f27

```html
<!DOCTYPE html>
<html lang="en">
<head>
<meta charset="utf-8">
<title>Bramble Hollow Networks – Electrical Flyer</title>
<link rel="stylesheet" href="https://fonts.googleapis.com/css2?family=Oswald:wght@600;700&family=Itim&display=swap">
<style>
  :root {
    --red: #ec1f27;
    --red-deep: #c1121a;
    --paper: #ececec;
    --white: #ffffff;
    --navy: #1d2740;
  }
  * { margin: 0; padding: 0; box-sizing: border-box; }
  html, body { width: 952px; height: 1200px; overflow: hidden; background: var(--paper); }
  .flyer { position: relative; width: 952px; height: 1200px; background: var(--paper); overflow: hidden; }
  .shapes { position: absolute; inset: 0; width: 952px; height: 1200px; }
  .call {
    position: absolute; left: 78px; top: 40px;
    transform: rotate(10deg); transform-origin: left top;
    font-family: "Oswald", sans-serif; color: var(--white); line-height: 1;
  }
  .call-name { font-size: 27px; font-weight: 600; letter-spacing: 1px; }
  .call-phone { font-size: 58px; font-weight: 700; letter-spacing: 1px; margin-top: 2px; margin-left: -24px; }
  .headline {
    position: absolute; left: 144px; top: 368px;
    font-family: "Oswald", sans-serif; font-weight: 700; color: var(--red); line-height: 1;
  }
  .headline-need { font-size: 118px; letter-spacing: -1px; }
  .headline-an { font-size: 52px; margin-left: 6px; }
  .headline-trade { display: block; font-size: 60px; margin-top: 6px; margin-left: -6px; letter-spacing: 0.5px; }
  .headline-rule {
    position: absolute; left: 217px; top: 543px; width: 318px; height: 3px;
    background: linear-gradient(90deg, rgba(236,31,39,0), var(--red) 60%);
  }
  .services { position: absolute; left: 410px; top: 702px; list-style: none; }
  .services li {
    display: flex; align-items: center; gap: 10px; height: 50px;
    font-family: "Itim", sans-serif; font-size: 27px; color: var(--white);
  }
  .services svg { width: 30px; height: 30px; flex: none; }
  .quote-cta {
    position: absolute; left: 36px; top: 1010px;
    transform: rotate(10deg); transform-origin: left top;
    font-family: "Oswald", sans-serif; font-weight: 700; font-size: 35px; color: var(--white); letter-spacing: 0.5px;
  }
  .licence {
    position: absolute; left: 610px; top: 1112px;
    transform: rotate(10deg); transform-origin: left top;
    font-family: "Oswald", sans-serif; font-weight: 700; font-size: 22px; color: var(--white);
  }
</style>
</head>
<body>
<div class="flyer">
  <svg class="shapes" viewBox="0 0 1402 1960" preserveAspectRatio="none" aria-hidden="false">
    <defs>
      <linearGradient id="bandRed" x1="0" y1="0" x2="1" y2="0">
        <stop offset="0" stop-color="#c81017"/>
        <stop offset="0.5" stop-color="#ec1f27"/>
        <stop offset="1" stop-color="#d8141c"/>
      </linearGradient>
      <linearGradient id="mainRed" x1="0" y1="0" x2="1" y2="1">
        <stop offset="0" stop-color="#c0111a"/>
        <stop offset="0.45" stop-color="#ec1f27"/>
        <stop offset="1" stop-color="#b80f17"/>
      </linearGradient>
      <linearGradient id="workerTone" x1="0" y1="0" x2="0" y2="1">
        <stop offset="0" stop-color="#e9822c"/>
        <stop offset="0.2" stop-color="#d9a98c"/>
        <stop offset="0.35" stop-color="#26304a"/>
        <stop offset="1" stop-color="#1d2740"/>
      </linearGradient>
      <linearGradient id="photoBoard" x1="0" y1="0" x2="1" y2="0">
        <stop offset="0" stop-color="#e4e4e6"/>
        <stop offset="1" stop-color="#c9ccd2"/>
      </linearGradient>
      <linearGradient id="photoTheatre" x1="0" y1="0" x2="1" y2="0">
        <stop offset="0" stop-color="#3b47c9"/>
        <stop offset="0.6" stop-color="#a9b0d8"/>
        <stop offset="1" stop-color="#f4f4f8"/>
      </linearGradient>
      <linearGradient id="photoOffice" x1="0" y1="0" x2="0" y2="1">
        <stop offset="0" stop-color="#f2f4f6"/>
        <stop offset="1" stop-color="#b9c3c2"/>
      </linearGradient>
    </defs>

    <polygon class="band-top" points="0,35 1402,318 1402,520 0,220" fill="url(#bandRed)"/>
    <polygon class="band-main" points="0,875 1402,1125 1402,1825 0,1585" fill="url(#mainRed)"/>
    <path class="tab-quote" d="M0,1560 L740,1700 L728,1830 Q724,1868 690,1862 L30,1742 Q0,1736 0,1706 Z" fill="var(--red)"/>
    <path class="tab-licence" d="M805,1700 L1290,1800 L1284,1900 Q1280,1932 1248,1926 L838,1850 Q805,1843 805,1810 Z" fill="var(--red)"/>

    <g role="img" aria-label="Photo of a smiling electrician in a hard hat and navy overalls holding a coil of orange cable">
      <path d="M600,60 Q900,20 1180,60 L1300,300 L1385,900 L1385,1150 L780,1090 L560,600 Z" fill="url(#workerTone)"/>
    </g>
    <g role="img" aria-label="Photo of circuit breakers being tested with a red probe">
      <polygon points="0,1075 595,1090 470,1232 0,1228" fill="url(#photoBoard)"/>
    </g>
    <g role="img" aria-label="Photo of a home theatre room with blue lighting and a projection screen">
      <polygon points="0,1245 560,1262 470,1400 0,1395" fill="url(#photoTheatre)"/>
    </g>
    <g role="img" aria-label="Photo of a bright open-plan office fitout with downlights">
      <polygon points="0,1415 535,1430 440,1570 0,1565" fill="url(#photoOffice)"/>
    </g>
  </svg>

  <div class="call">
    <div class="call-name">CALL LEOPOLD</div>
    <div class="call-phone">0438917062</div>
  </div>

  <h1 class="headline">
    <span class="headline-need">NEED</span><span class="headline-an">AN</span>
    <span class="headline-trade">ELECTRICIAN?</span>
  </h1>
  <div class="headline-rule"></div>

  <ul class="services">
    <li><svg viewBox="0 0 30 30"><circle cx="15" cy="15" r="13" fill="none" stroke="#fff" stroke-width="2.2"/><path d="M18 5 L9 17 H15 L12 25 L21 13 H15 Z" fill="#fff"/></svg>Office fitouts</li>
    <li><svg viewBox="0 0 30 30"><circle cx="15" cy="15" r="13" fill="none" stroke="#fff" stroke-width="2.2"/><path d="M18 5 L9 17 H15 L12 25 L21 13 H15 Z" fill="#fff"/></svg>Switchboard upgrades</li>
    <li><svg viewBox="0 0 30 30"><circle cx="15" cy="15" r="13" fill="none" stroke="#fff" stroke-width="2.2"/><path d="M18 5 L9 17 H15 L12 25 L21 13 H15 Z" fill="#fff"/></svg>Installation of ceiling fans</li>
    <li><svg viewBox="0 0 30 30"><circle cx="15" cy="15" r="13" fill="none" stroke="#fff" stroke-width="2.2"/><path d="M18 5 L9 17 H15 L12 25 L21 13 H15 Z" fill="#fff"/></svg>Powerpoint and downlight upgrades</li>
    <li><svg viewBox="0 0 30 30"><circle cx="15" cy="15" r="13" fill="none" stroke="#fff" stroke-width="2.2"/><path d="M18 5 L9 17 H15 L12 25 L21 13 H15 Z" fill="#fff"/></svg>Home theatre and AV systems</li>
    <li><svg viewBox="0 0 30 30"><circle cx="15" cy="15" r="13" fill="none" stroke="#fff" stroke-width="2.2"/><path d="M18 5 L9 17 H15 L12 25 L21 13 H15 Z" fill="#fff"/></svg>All exterior and emergency work</li>
  </ul>

  <div class="quote-cta">GET FREE QUOTES TODAY</div>
  <div class="licence">LICENCE NO : 63914K</div>
</div>
</body>
</html>
```